modernized upgrade to existing squarespace site

Hello! I have the following page for my consulting firm: https://fernwaystrategygroup.com/ Would love to upgrade to something more modern/attractive like here: https://www.lobrettiandco.com/ or https://quillbrightlab.com/ , but I am open to creativity. Would like to retain the logo look and color theme from the logo. The rest can be left to creative discretion.

```html
<!DOCTYPE html>
<html lang="en">
<head>
<meta charset="utf-8">
<title>Fernway Strategy Group</title>
<link rel="stylesheet" href="https://fonts.googleapis.com/css2?family=Prata&family=Poppins:wght@400;500&family=Playfair+Display:ital@1&display=swap">
<style>
:root{
  --accent:#c77b6d;
  --accent-dark:#b86a5c;
  --blush:#fdf1ef;
  --ink:#2b2b2b;
  --muted:#555;
  --line:#9a9a9a;
  --dark:#2f2f2f;
  --white:#fff;
}
*{box-sizing:border-box;margin:0;padding:0}
html,body{width:1200px;height:5277px;overflow:hidden}
body{position:relative;background:var(--white);font-family:'Poppins',sans-serif;color:var(--ink)}
.abs{position:absolute}
.serif{font-family:'Prata',serif;font-weight:400}
.btn{position:absolute;display:flex;align-items:center;justify-content:center;border-radius:30px;font-family:'Prata',serif;font-size:16px;color:var(--white);background:var(--accent);white-space:nowrap}
.btn.ghost{background:transparent;border:2px solid var(--accent);color:var(--ink)}
.btn.light{background:transparent;border:2px solid var(--white);color:var(--white)}

/* hero */
.hero{left:0;top:0;width:1200px;height:657px;background:linear-gradient(120deg,#d9dee2 0%,#c4ccd2 35%,#9aa3aa 70%,#7c858c 100%)}
.hero-shade{left:0;top:0;width:1200px;height:657px;background:linear-gradient(90deg,rgba(255,255,255,.55),rgba(255,255,255,0) 55%)}
.brand-mark{left:86px;top:20px;width:58px;height:58px;border:2px solid var(--accent);background:rgba(255,255,255,.6)}
.brand-name{left:160px;top:22px;font-family:'Prata',serif;color:var(--ink);font-size:28px;letter-spacing:3px;line-height:1.1}
.brand-name small{display:block;font-size:13px;letter-spacing:3px;margin-top:2px}
.nav{left:0;top:31px;width:1200px;height:24px;font-family:'Prata',serif;font-size:16px}
.nav span{position:absolute;top:0;color:var(--ink);white-space:nowrap}
.nav .active{color:var(--accent)}
.hero-title{left:126px;top:186px;font-size:54px;line-height:1.3;color:#222;white-space:nowrap}
.hero-sub{left:130px;top:336px;font-size:19px;color:#333}
.arrow{top:268px}

/* sample band */
.band{left:0;top:657px;width:1200px;height:355px;background:linear-gradient(90deg,#3a3a3a,#2d2d2d 60%,#354040)}
.band-text{left:0;top:728px;width:1200px;text-align:center;font-size:44px;line-height:64px;color:var(--white);white-space:nowrap}

/* section headings */
.sec-title{font-size:46px;left:86px;color:var(--ink);white-space:nowrap}
.sec-rule{left:86px;width:1028px;height:2px;background:var(--line)}
.ghost-word{font-family:'Prata',serif;font-size:150px;color:rgba(199,123,109,.12);line-height:1;white-space:nowrap}
.ghost-box{border:6px solid rgba(199,123,109,.12)}

/* cards */
.card{position:absolute;width:330px;height:438px;border:2px solid #e3e3e3;background:var(--white)}
.card .ph{position:absolute;left:12px;top:12px;width:304px;height:207px}
.card h3{position:absolute;left:18px;top:238px;font-family:'Prata',serif;font-weight:400;font-size:22px;white-space:nowrap}
.card p{position:absolute;left:18px;top:280px;width:290px;font-size:15px;line-height:26px;color:var(--muted)}
.card .btn{left:18px;top:366px;width:154px;height:44px}

.blush{left:0;width:1200px;background:var(--blush)}

/* institute */
.inst-panel{left:135px;top:1913px;width:930px;height:547px;background:var(--accent)}
.inst-photo{left:135px;top:1913px;width:460px;height:547px;background:linear-gradient(180deg,#b06f63,#8f5a50)}
.inst-title{left:610px;top:1950px;font-size:54px;line-height:84px;color:var(--white);white-space:nowrap}
.inst-tag{left:610px;top:2218px;font-family:'Playfair Display',serif;font-style:italic;font-size:27px;color:var(--white);white-space:nowrap}
.inst-copy{left:610px;top:2270px;width:440px;font-size:16px;line-height:34px;color:var(--white)}

/* news */
.news-panel{left:135px;top:3383px;width:930px;height:549px;background:var(--accent)}
.news-photo{left:720px;top:3383px;width:345px;height:549px;background:linear-gradient(180deg,#c98a7e,#b57468)}
.news-quote{left:168px;top:3430px;font-size:40px;line-height:73px;color:var(--white);white-space:nowrap}
.news-src{left:168px;top:3824px;font-size:19px;color:var(--white)}
.news-src:before{content:"";display:inline-block;width:50px;height:2px;background:var(--white);vertical-align:middle;margin-right:18px}

/* seen on */
.seen-title{left:0;top:4030px;width:1200px;text-align:center;font-size:36px;color:var(--ink)}
.outlets{left:86px;top:4110px;width:1028px;display:flex;justify-content:space-between;align-items:center;height:60px}
.outlets span{font-family:'Prata',serif;font-size:19px;color:#3a3a3a;white-space:nowrap}

/* newsletter */
.news-box{left:135px;top:4282px;width:930px;height:275px;background:linear-gradient(135deg,#c98375,#c17365)}
.nl-title{left:168px;top:4318px;font-size:44px;line-height:58px;color:var(--white);white-space:nowrap}
.nl-copy{left:170px;top:4452px;width:320px;font-size:15px;line-height:32px;color:var(--white)}
.nl-input{left:512px;top:4427px;width:334px;height:40px;padding-top:8px;border-bottom:2px solid rgba(255,255,255,.8);font-size:15px;color:rgba(255,255,255,.85)}

/* footer */
.footer{left:0;top:4612px;width:1200px;height:665px;background:var(--dark);color:#ddd}
.f-col{position:absolute;top:4684px;font-size:14px;line-height:29px;color:#e6e6e6;white-space:nowrap}
.f-col h4{font-family:'Prata',serif;font-weight:400;font-size:16px;margin-bottom:22px;color:var(--white)}
.f-rule{left:307px;top:4936px;width:584px;height:1px;background:#777}
.f-about{left:182px;top:4988px;width:840px;font-size:15px;line-height:29px;color:#ddd}
.f-copy{left:86px;top:5224px;font-size:12px;color:#aaa}
.f-copy b{color:#ddd;font-weight:500}
</style>
</head>
<body>

<!-- hero -->
<div class="abs hero" role="img" aria-label="Photo of a team of six business professionals standing on a glass terrace overlooking a city"></div>
<div class="abs hero-shade"></div>
<div class="abs brand-mark"></div>
<div class="abs brand-name">FERNWAY<small>STRATEGY GROUP</small></div>
<nav class="abs nav">
  <span class="active" style="left:380px">Home</span>
  <span style="left:472px">Services</span>
  <span style="left:580px">Research</span>
  <span style="left:692px">The Institute</span>
  <span style="left:840px">In the News</span>
</nav>
<div class="btn" style="left:962px;top:22px;width:152px;height:46px">Contact Us</div>
<h1 class="abs hero-title serif">Macroeconomic<br>&amp; policy analytics</h1>
<div class="abs hero-sub">For today's turbulent environment</div>
<div class="btn" style="left:128px;top:394px;width:164px;height:46px">Discover More</div>
<svg class="abs arrow" style="left:82px" width="40" height="80" viewBox="0 0 40 80"><polyline points="34,4 6,40 34,76" fill="none" stroke="#fff" stroke-width="3"/></svg>
<svg class="abs arrow" style="left:1076px" width="40" height="80" viewBox="0 0 40 80"><polyline points="6,4 34,40 6,76" fill="none" stroke="#fff" stroke-width="3"/></svg>

<!-- sample band -->
<div class="abs band" role="img" aria-label="Darkened photo of a professional reviewing data on a screen"></div>
<p class="abs band-text serif">Most of our work product is proprietary,<br>but feel free to reach out for additional samples.</p>
<div class="btn" style="left:366px;top:880px;width:228px;height:44px">Industry Impact Sample</div>
<div class="btn light" style="left:606px;top:880px;width:228px;height:44px">Empirical Study Sample</div>

<!-- what we do -->
<div class="abs ghost-box" style="left:86px;top:1048px;width:396px;height:300px"></div>
<h2 class="abs sec-title serif" style="top:1062px">What We Do</h2>
<div class="abs sec-rule" style="top:1139px"></div>
<div class="card" style="left:86px;top:1200px">
  <div class="ph" role="img" aria-label="Laptop showing analytics charts" style="background:linear-gradient(135deg,#2a2230,#4a2d3e)"></div>
  <h3>Analytics &amp; Messaging</h3>
  <p>Our communications team can develop influential messaging, in conjunction with our data</p>
  <div class="btn">Read More</div>
</div>
<div class="card" style="left:434px;top:1200px">
  <div class="ph" role="img" aria-label="Hand holding a printed report with charts" style="background:linear-gradient(135deg,#d5dde4,#7f8a95)"></div>
  <h3>Customized Reports</h3>
  <p>From succinct summations of economic and policy impact to full-length analyses, we can create</p>
  <div class="btn">Read More</div>
</div>
<div class="card" style="left:784px;top:1200px">
  <div class="ph" role="img" aria-label="Colleagues reviewing a survey on a monitor" style="background:linear-gradient(135deg,#e4ebee,#9fb1b9)"></div>
  <h3>Proprietary Surveys</h3>
  <p>Exclusive, custom-designed surveys can enrich your databank, while maintaining access</p>
  <div class="btn">Read More</div>
</div>

<!-- institute -->
<div class="abs blush" style="top:1669px;height:821px"></div>
<div class="abs ghost-word" style="left:92px;top:1810px">Institute</div>
<h2 class="abs sec-title serif" style="top:1730px">The Institute</h2>
<div class="abs sec-rule" style="top:1806px"></div>
<div class="abs inst-panel"></div>
<div class="abs inst-photo" role="img" aria-label="Photo of two smiling business professionals standing back to back"></div>
<h2 class="abs inst-title serif">Thoughtful<br>Solutions that<br>Bridge</h2>
<div class="abs inst-tag">the academic with private industry.</div>
<p class="abs inst-copy">The Fernway Policy Institute (FPI) is an independent non-profit organization that partners</p>
<div class="btn light" style="left:610px;top:2350px;width:206px;height:53px;font-size:22px">Read More</div>

<!-- research -->
<div class="abs ghost-word" style="left:86px;top:2530px">Research</div>
<h2 class="abs sec-title serif" style="top:2545px">Research</h2>
<div class="abs sec-rule" style="top:2621px"></div>
<div class="card" style="left:86px;top:2673px">
  <div class="ph" role="img" aria-label="Telecommunications tower against a blue sky" style="background:linear-gradient(180deg,#4b7fb8,#a9c7e2)"></div>
  <h3>Telecommunications</h3>
  <p>We are in the age of unprecedented technological shifts in telecommunications. Unfortunately</p>
  <div class="btn">Read More</div>
</div>
<div class="card" style="left:434px;top:2673px">
  <div class="ph" role="img" aria-label="Professionals working at desks in an office" style="background:linear-gradient(135deg,#d9dcdf,#8e959c)"></div>
  <h3>Fiscal Policy</h3>
  <p>From municipal to federal, our fiscal policy expertise has spanned decades, while our analytical</p>
  <div class="btn">Read More</div>
</div>
<div class="card" style="left:784px;top:2673px">
  <div class="ph" role="img" aria-label="Shopping cart in front of a world trade graphic" style="background:linear-gradient(135deg,#8d9aa6,#3f4a55)"></div>
  <h3>Retail and trade</h3>
  <p>Trade policies are ever-evolving, impacting our companies in unforeseen and oftentimes</p>
  <div class="btn">Read More</div>
</div>

<!-- news -->
<div class="abs blush" style="top:3140px;height:823px"></div>
<div class="abs ghost-box" style="left:86px;top:3195px;width:460px;height:400px"></div>
<h2 class="abs sec-title serif" style="top:3202px">In the News</h2>
<div class="btn ghost" style="left:954px;top:3212px;width:160px;height:44px">View All</div>
<div class="abs sec-rule" style="top:3279px"></div>
<div class="abs news-panel"></div>
<div class="abs news-photo" role="img" aria-label="Photo of a smiling businessman in a light grey suit"></div>
<p class="abs news-quote serif">“Medical Technology<br>Industry Continues to<br>Create High-Paying<br>Jobs at Small Businesses<br>Throughout Pandemic.”</p>
<div class="abs news-src">Clinical Imaging Review</div>

<!-- seen on -->
<h2 class="abs seen-title serif">As Seen On...</h2>
<div class="abs outlets">
  <span>Ledgerline</span><span>Capitol Desk</span><span>Metro Wire</span><span>Public Airwaves</span><span>Channel Nine</span><span>Market Pulse</span><span>Finora</span>
</div>

<!-- newsletter -->
<div class="abs news-box"></div>
<h2 class="abs nl-title serif">Subscribe to<br>Our Newsletter</h2>
<p class="abs nl-copy">Sign up with your email address to receive news and updates.</p>
<div class="abs nl-input">Email address</div>
<div class="btn light" style="left:850px;top:4420px;width:164px;height:47px">Sign Up</div>

<!-- footer -->
<footer class="abs footer"></footer>
<div class="f-col" style="left:86px"><h4>Useful Links</h4>Home<br>Services<br>Research<br>The Institute<br>In the News<br>Contact Us</div>
<div class="f-col" style="left:334px"><h4>Contact Info</h4>418 Linden Row<br>Suite 210<br>Harborton, MD 21904<br><span style="display:block;margin-top:14px">info@fernwaystrategygroup.com</span></div>
<div class="f-col" style="left:700px"><h4>Services</h4>Analytics &amp; Messaging<br>Customized Reports<br>Proprietary Surveys</div>
<div class="f-col" style="left:1012px"><h4>Get In Touch</h4><span style="display:inline-block;width:16px;height:16px;background:#e6e6e6;margin-left:2px"></span></div>
<div class="abs f-rule"></div>
<p class="abs f-about">Our services suite focuses on providing exclusive, custom research and analytics to a select number of clients. We do so by outlining a sophisticated research plan, building teams of industry experts, and providing final analyses catered to your preferred audience. There is no one-size approach to economic policy research, as such we maintain an ongoing exchange of findings and viewpoints, involving your deep industry knowledge and direction throughout the life of a proposed project.</p>
<div class="abs f-copy">© 2024 <b>Fernway Strategy Group</b>. All right reserved</div>

</body>
</html>
```